Spa needs a storefront sticker design

For our city spa we need window stickers for the shop window.
The window stickers must fill the entire windows.
What we have in mind is that our logo is visible in the middle with graphic shapes surrounding it to stand out extra on the main street. The design is going to be printed in white and cut out. To give an impression of what we have in mind, our logo is attached with various example designs.
please supply your final file in the following extensions: – Eps file (*.eps) – Photoshop file (*.psd) – Adobe Portable Document (*.pdf) – Jpeg file ( *.jpg, *.jpeg) – Tiff file (*.tif, *.tiff)– Text in letter outlines
A photo of the shop window will be added tomorrow, including the exact dimensions so that the design can be adjusted accordingly
Look and feel
Each slider illustrates characteristics of the customer's brand and the style your logo design should communicate.

```html
<!DOCTYPE html>
<html lang="en">
<head>
<meta charset="utf-8">
<title>Willow Baby &amp; Spa – Window Sticker</title>
<link href="https://fonts.googleapis.com/css2?family=Marcellus&display=swap" rel="stylesheet">
<style>
  :root {
    --paper: #ffffff;
    --ink: #383838;
    --floral-light: #f1f1f1;
    --floral-mid: #e2e2e2;
  }
  html, body {
    margin: 0;
    padding: 0;
    overflow: hidden;
    background: var(--paper);
  }
  .sticker {
    position: relative;
    width: 1200px;
    height: 778px;
    background: var(--paper);
    overflow: hidden;
  }
  .floral {
    position: absolute;
    background: radial-gradient(ellipse at center, var(--floral-mid) 0%, var(--floral-light) 70%, rgba(241,241,241,0) 100%);
  }
  .floral--top {
    left: 16px; top: -20px; width: 650px; height: 250px;
    border-radius: 0 0 50% 50% / 0 0 60% 60%;
  }
  .floral--top-right {
    right: -20px; top: -20px; width: 400px; height: 470px;
    border-radius: 0 0 0 60% / 0 0 0 50%;
  }
  .floral--bottom-left {
    left: -20px; bottom: -20px; width: 390px; height: 500px;
    border-radius: 0 60% 0 0 / 0 45% 0 0;
  }
  .floral--bottom-right {
    left: 360px; bottom: -20px; width: 820px; height: 290px;
    border-radius: 50% 50% 0 0 / 60% 60% 0 0;
  }
  .brand {
    position: absolute;
    left: 0;
    top: 318px;
    width: 1200px;
    text-align: center;
    color: var(--ink);
    font-family: "Marcellus", serif;
    font-weight: 400;
  }
  .brand__name {
    margin: 0;
    font-size: 84px;
    line-height: 1;
    letter-spacing: 0.14em;
    padding-left: 0.14em;
  }
  .brand__tagline {
    margin: 34px 0 0;
    font-size: 27px;
    line-height: 1;
    letter-spacing: 0.03em;
  }
</style>
</head>
<body>
  <main class="sticker">
    <div class="floral floral--top" role="img" aria-label="Line-drawn flowering branch with open blossoms, buds and leaves along the top edge"></div>
    <div class="floral floral--top-right" role="img" aria-label="Line-drawn flowering branch with blossoms and buds in the top right corner"></div>
    <div class="floral floral--bottom-left" role="img" aria-label="Line-drawn flowering branch with blossoms and buds in the bottom left corner"></div>
    <div class="floral floral--bottom-right" role="img" aria-label="Line-drawn flowering branch with a large blossom, buds and leaves along the bottom edge"></div>

    <div class="brand">
      <h1 class="brand__name">WILLOW</h1>
      <p class="brand__tagline">Baby &amp; Spa</p>
    </div>
  </main>
</body>
</html>
```